Clara Joy Halden- Lantern Waltz- Autumn/Winter Tour Dates

I need high res A3 Tour poster for print and for social media JPG sharing of tour dates.
Also needed Facebook/Twitter Banner Cover Photos of these dates.
Text Needed Below
Clara Joy Halden
Lantern Waltz
Autumn/Winter Tour Dates
03/09 Ravensby Folk Festival
21/09 Swindon- Calder Theatre
01/10 Hitchin- Brackwell Folk Club
17/10 Bath- The Anvil
20/10 Sheffield- Upper Dale Croquet Club
24/10 Birmingham- Orchard Lamp Cafe
26/10 Glasgow- The Nook and Jar
27/10 Edinburgh - The Marble Parlour
08/11 Capital Reel and Ballad Festival- The Crooked Heron
25/11 Lewes- Tandem Record Shop- Live In Store
02/12 Cambridge- The Quayside
27/01 Lincolnshire- Fenmarsh Theatre
Tickets/Info: www.clarajoyhalden-music.example/gigs
(Quotes/Reviews To Put On)
"Outstanding, rich and expressive."            "Vibrant and Experimental"
**** BdM                                                               **** Tunepaths
"Impressive and Invigorating"                        "Enchanting" Acoustic Wire UK
tBarks

Updates
I cannot read the tour dates on most of the submissions so far. They need to be visible to viewers.
Thank You.
Please also be as creative and inventive as possible- not bland.

Target Market(s)
Music Fans- Folk Acoustic Americana
Industry/Entity Type
Media
Font styles to use
Requirements
Must have
- My photo featured prominently
- Look classy and not tacky or OTT
- Look elegant, wintery and eye catching
- The dates must be very clear to read
- Links to Website:

Nice to have
- Something innovative and not boring in terms of layout design
- Perhaps fading/ misty or wintery

Should not have
- Any colours that do not match

```html
<!DOCTYPE html>
<html lang="en">
<head>
<meta charset="utf-8">
<title>Clara Joy Halden – Lantern Waltz Tour Poster</title>
<link rel="stylesheet" href="https://fonts.googleapis.com/css2?family=Great+Vibes&family=Cinzel:wght@400&family=Lato:wght@400&display=swap">
<style>
  :root {
    --stage: #d9dadc;
    --night: #07090f;
    --ink-deep: #0d1220;
    --mist: #2a3550;
    --ice: #cfd9f2;
    --band-blue: #4660b4;
    --band-edge: #8aa0e0;
    --date-blue: #8fa6e6;
    --white: #ffffff;
  }
  * { box-sizing: border-box; margin: 0; padding: 0; }
  html, body { width: 1200px; height: 861px; overflow: hidden; background: var(--stage); }
  .poster {
    position: absolute; left: 313px; top: 2px; width: 574px; height: 858px;
    background: var(--night); overflow: hidden; font-family: "Lato", sans-serif; color: var(--white);
  }
  .portrait {
    position: absolute; left: 0; top: 125px; width: 574px; height: 650px;
    background:
      radial-gradient(ellipse 200px 230px at 260px 200px, #4a5678 0%, #26304a 45%, rgba(13,18,32,0) 80%),
      radial-gradient(ellipse 300px 320px at 420px 390px, #1e2740 0%, rgba(7,9,15,0) 75%),
      linear-gradient(180deg, var(--night) 0%, var(--ink-deep) 25%, var(--mist) 50%, var(--ink-deep) 80%, var(--night) 100%);
  }
  .artist {
    position: absolute; left: 0; width: 100%; top: 24px; text-align: center;
    font-family: "Great Vibes", cursive; font-weight: 400; font-size: 62px; line-height: 1.15; color: var(--white);
  }
  .album-title {
    position: absolute; left: 54px; width: 466px; top: 104px;
    display: flex; align-items: center; gap: 12px;
    font-family: "Cinzel", serif; font-size: 24px; letter-spacing: 3px; color: var(--ice);
  }
  .album-title::before, .album-title::after { content: ""; flex: 1; height: 2px; background: var(--white); }
  .tour-band { position: absolute; left: 0; top: 413px; }
  .tour-heading {
    position: absolute; left: 20px; top: 419px;
    font-size: 24px; font-weight: 400; color: var(--white);
  }
  .dates { position: absolute; left: 20px; top: 460px; list-style: none; font-size: 17px; line-height: 21.9px; }
  .dates .date { color: var(--date-blue); margin-right: 5px; }
  .tickets { position: absolute; left: 20px; top: 750px; font-size: 17.5px; white-space: nowrap; }
  .tickets .label { color: var(--date-blue); }
  .quotes-band { position: absolute; left: 0; top: 778px; }
  .quotes {
    position: absolute; left: 20px; top: 786px; font-size: 11px; line-height: 17px; color: var(--white);
  }
  .album-cover {
    position: absolute; left: 459px; top: 758px; width: 96px; height: 96px; border-radius: 50%;
    border: 2px solid var(--band-edge);
    background: radial-gradient(circle at 50% 45%, #3a4668 0%, #141a2c 70%, #07090f 100%);
  }
</style>
</head>
<body>
<main class="poster">
  <div class="portrait" role="img" aria-label="Portrait of the singer wearing a pearl and wire crown in a misty winter forest"></div>

  <h1 class="artist">Clara Joy Halden</h1>
  <p class="album-title">Lantern Waltz</p>

  <svg class="tour-band" width="360" height="40" viewBox="0 0 360 40" aria-hidden="true">
    <polygon points="0,0 340,0 325,38 0,38" fill="var(--band-blue)"/>
    <line x1="340" y1="0" x2="354" y2="38" stroke="var(--band-edge)" stroke-width="2"/>
  </svg>
  <h2 class="tour-heading">Autumn/Winter Tour Dates</h2>

  <ul class="dates">
    <li><span class="date">03/09</span>Ravensby Folk Festival</li>
    <li><span class="date">21/09</span>Swindon- Calder Theatre</li>
    <li><span class="date">01/10</span>Hitchin- Brackwell Folk Club</li>
    <li><span class="date">17/10</span>Bath- The Anvil</li>
    <li><span class="date">20/10</span>Sheffield- Upper Dale Croquet Club</li>
    <li><span class="date">24/10</span>Birmingham- Orchard Lamp Cafe</li>
    <li><span class="date">26/10</span>Glasgow- The Nook and Jar</li>
    <li><span class="date">27/10</span>Edinburgh - The Marble Parlour</li>
    <li><span class="date">08/11</span>Capital Reel and Ballad Festival- The Crooked Heron</li>
    <li><span class="date">25/11</span>Lewes- Tandem Record Shop- Live In Store</li>
    <li><span class="date">02/12</span>Cambridge- The Quayside</li>
    <li><span class="date">27/01</span>Lincolnshire- Fenmarsh Theatre</li>
  </ul>

  <p class="tickets"><span class="label">Tickets/Info:</span> www.clarajoyhalden-music.example/gigs</p>

  <svg class="quotes-band" width="574" height="54" viewBox="0 0 574 54" aria-hidden="true">
    <line x1="0" y1="1" x2="574" y2="1" stroke="var(--band-edge)" stroke-width="2"/>
    <rect x="0" y="4" width="574" height="44" fill="var(--band-blue)"/>
    <line x1="0" y1="51" x2="574" y2="51" stroke="var(--band-edge)" stroke-width="2"/>
  </svg>
  <p class="quotes">
    "Outstanding, rich and expressive." "Vibrant and Experimental" *** BdM *** Tunepaths<br>
    "Impressive and Invigorating" "Enchanting" Acoustic Wire UK tBarks
  </p>
  <div class="album-cover" role="img" aria-label="Lantern Waltz album cover artwork"></div>
</main>
</body>
</html>
```